Lena Corvel Business Card

I need a business card that reflects my current website: itslenacorvel.com and screenshot attached. If we keep the color scheme of the site and sample card below that would be ideal. The business card should include the information on the attached sample cards.

Industry/Entity Type

Business

```html
<!DOCTYPE html>
<html lang="en">
<head>
<meta charset="utf-8">
<title>Lena Corvel Business Card</title>
<link rel="stylesheet" href="https://fonts.googleapis.com/css2?family=Lato:wght@300;400&family=Open+Sans:wght@400&display=swap">
<style>
  :root {
    --card-bg: #f2f2f2;
    --slate: #535a66;
    --teal: #5fb8a8;
    --ink: #4a4a4a;
    --logo-ink: #1e1e1e;
    --white: #ffffff;
  }
  html, body {
    margin: 0;
    padding: 0;
    overflow: hidden;
    background: var(--card-bg);
  }
  .card {
    position: relative;
    width: 1200px;
    height: 753px;
    background: var(--card-bg);
    overflow: hidden;
  }
  .side-bar {
    position: absolute;
    left: 0;
    top: 0;
    width: 44px;
    height: 753px;
    background: var(--slate);
  }
  .side-accent {
    position: absolute;
    left: 0;
    top: 393px;
    width: 44px;
    height: 57px;
    background: var(--teal);
    border-top: 5px solid var(--white);
    border-bottom: 5px solid var(--white);
  }
  .name-band {
    position: absolute;
    left: 542px;
    top: 393px;
    width: 658px;
    height: 57px;
    background: var(--teal);
    border-top: 5px solid var(--white);
  }
  .brand {
    position: absolute;
    right: 54px;
    top: 104px;
    text-align: right;
  }
  .brand-name {
    font-family: "Lato", sans-serif;
    font-weight: 400;
    font-size: 31px;
    color: var(--logo-ink);
    line-height: 1;
    margin: 0 0 10px;
  }
  .brand-tagline {
    font-family: "Open Sans", sans-serif;
    font-size: 14.5px;
    color: var(--ink);
    margin: 0;
    white-space: nowrap;
  }
  .brand-square {
    position: absolute;
    right: 0;
    top: 116px;
    width: 49px;
    height: 59px;
    background: var(--slate);
  }
  .person-name {
    position: absolute;
    left: 91px;
    top: 396px;
    margin: 0;
    font-family: "Lato", sans-serif;
    font-weight: 300;
    font-size: 56px;
    letter-spacing: 6px;
    line-height: 60px;
    color: var(--teal);
    white-space: nowrap;
  }
  .contact {
    position: absolute;
    left: 92px;
    top: 486px;
    margin: 0;
    padding: 0;
    list-style: none;
    font-family: "Open Sans", sans-serif;
    font-size: 24px;
    line-height: 40.5px;
    color: var(--ink);
  }
</style>
</head>
<body>
  <div class="card">
    <div class="side-bar"></div>
    <div class="side-accent"></div>

    <div class="brand">
      <p class="brand-name">its Lena Corvel</p>
      <p class="brand-tagline">Brand Curator | Digital Storyteller | Social Entrpreneuer</p>
    </div>
    <div class="brand-square"></div>

    <h1 class="person-name">LENA CORVEL</h1>
    <div class="name-band"></div>

    <ul class="contact">
      <li>me@lenacorvel.com</li>
      <li>555.014.2270</li>
      <li>[fb] | [t.] | [ig] @itslenacorvel</li>
      <li>www.itslenacorvel.com</li>
    </ul>
  </div>
</body>
</html>
```